Custom workshop/manufacture for custom furniture, architectural millwork and kitchen cabinetry

simple and clean. I like this website:
http://www.velmarostudio.com

Attached are random ideas

Target Market(s)

residential, commercial, hospitality, interior designers, architects, contractors

Coding

Coded - Design and coding required

Number of Pages Required

5+ page

Font styles to use
Other font styles liked:
• Avenir next

Requirements
Must have
• drop down menu for work - residential - commercial

```html
<!DOCTYPE html>
<html lang="en">
<head>
<meta charset="utf-8">
<title>Furniture co. — custom furniture</title>
<link rel="stylesheet" href="https://fonts.googleapis.com/css2?family=Montserrat:wght@500;600;700&family=Open+Sans:wght@400;600&display=swap">
<style>
  :root{
    --ink:#111111;
    --white:#ffffff;
    --muted:#9a9a9a;
    --rule:#d8d8d8;
    --stage:#ffffff;
  }
  *{margin:0;padding:0;box-sizing:border-box}
  html,body{width:1200px;height:1200px;overflow:hidden;background:var(--stage)}
  body{font-family:"Open Sans",sans-serif;color:var(--ink);position:relative}
  .page{position:absolute;left:350px;top:4px;width:506px;height:1196px;background:var(--white);box-shadow:0 0 22px rgba(0,0,0,.28);overflow:hidden}
  .abs{position:absolute}
  .head{font-family:"Montserrat",sans-serif;font-weight:600;letter-spacing:-.2px}

  .nav{left:0;top:0;width:506px;height:25px;background:var(--white);z-index:3}
  .brand{left:86px;top:6px;display:flex;align-items:center;gap:5px;font-size:10px;font-weight:400}
  .brand-dot{width:11px;height:11px;border:1px solid var(--ink);border-radius:50%}
  .menu{right:62px;top:10px;display:flex;gap:12px;font-size:4px;font-weight:600;letter-spacing:.2px}

  .band{left:0;width:506px}
  .hero-title{left:86px;top:68px;font-size:32px;line-height:28px;color:var(--white)}
  .hero-sub{left:86px;top:134px;width:215px;font-size:5.5px;line-height:7.5px;color:var(--white)}
  .btn{display:flex;align-items:center;justify-content:center;background:var(--ink);color:var(--white);font-family:"Montserrat",sans-serif;font-weight:700;font-size:4.5px;border-radius:8px}
  .hero-btn{left:86px;top:157px;width:57px;height:16px}

  .feature{width:100px;text-align:center}
  .feature svg{display:block;margin:0 auto 5px}
  .feature h3{font-family:"Montserrat",sans-serif;font-size:6px;font-weight:500}
  .feature p{margin:4px auto 0;width:88px;font-size:5px;line-height:7.5px;color:#b5b5b5}

  .dream{left:0;width:506px;top:370px;text-align:center;font-size:25px;line-height:22px;color:var(--white)}

  .offer{left:86px;top:505px;font-size:22px}
  .label{font-size:3.5px;color:var(--ink)}
  .label-rule{height:.6px;background:#888}
  .list{font-size:5.5px;line-height:9.6px;color:var(--muted)}

  .tile{position:absolute}

  .news{left:86px;top:900px;font-size:25px;line-height:21px}
  .post{font-size:4.5px}
  .date{font-size:3px;color:var(--muted)}

  .ready{left:86px;top:1078px;font-size:26px;color:var(--white)}
  .ready-sub{left:86px;top:1109px;width:230px;font-size:5.5px;line-height:7.8px;color:var(--white)}
  .ready-btn{left:86px;top:1134px;width:68px;height:15px}
</style>
</head>
<body>
<div class="page">

  <header class="nav abs">
    <div class="brand abs"><span class="brand-dot"></span>Furniture co.</div>
    <nav class="menu abs"><span>HOME</span><span>ABOUT US</span><span>BLOG</span><span>MEMBERSHIP</span><span>CONTACT US</span></nav>
  </header>

  <svg class="band abs" style="top:25px" width="506" height="196" role="img" aria-label="Photo of a living room with a brown leather lounge chair, ottoman and a vase of dry branches">
    <defs>
      <linearGradient id="heroFill" x1="0" y1="0" x2="0.35" y2="1">
        <stop offset="0" stop-color="#8c7f6c"/>
        <stop offset=".45" stop-color="#a1937d"/>
        <stop offset=".7" stop-color="#6a4a3a"/>
        <stop offset="1" stop-color="#4a3226"/>
      </linearGradient>
    </defs>
    <polygon points="0,0 506,0 506,148 0,195" fill="url(#heroFill)"/>
  </svg>
  <h1 class="hero-title head abs">custom<br>furniture</h1>
  <p class="hero-sub abs">Custom workshop/manufacture for custom furniture, architectural millwork and kitchen cabinetry</p>
  <a class="hero-btn btn abs">MORE ABOUT US</a>

  <section>
    <div class="feature abs" style="left:86px;top:244px">
      <svg width="14" height="22" viewBox="0 0 14 22" fill="none" stroke="#111" stroke-width="1"><path d="M7 1a6 6 0 0 0-3.5 10.8V15h7v-3.2A6 6 0 0 0 7 1z"/><path d="M4 17.5h6M5 20h4M5 8l2 3 2-3M7 11v4"/></svg>
      <h3>creative designs</h3>
      <p>Short description regarding this feature of workshop / furnitures</p>
    </div>
    <div class="feature abs" style="left:203px;top:244px">
      <svg width="14" height="22" viewBox="0 0 14 22" fill="none" stroke="#111" stroke-width="1"><rect x="1.5" y="1" width="11" height="20" rx="1.5"/><path d="M5 3h4"/></svg>
      <h3>support services</h3>
      <p>Short description regarding this feature of workshop / furnitures</p>
    </div>
    <div class="feature abs" style="left:320px;top:244px">
      <svg width="22" height="22" viewBox="0 0 22 22" fill="none" stroke="#111" stroke-width="1"><path d="M2 7h18l-1 14H3z"/><path d="M7 9V5a4 4 0 0 1 8 0v4"/></svg>
      <h3>online ordering</h3>
      <p>Short description regarding this feature of workshop / furnitures</p>
    </div>
  </section>

  <svg class="band abs" style="top:320px" width="506" height="148" role="img" aria-label="Photo of a bright studio with a wooden easel, green sofa and dried branches">
    <defs>
      <linearGradient id="dreamFill" x1="0" y1="0" x2="0.2" y2="1">
        <stop offset="0" stop-color="#a09d92"/>
        <stop offset=".45" stop-color="#77776e"/>
        <stop offset=".8" stop-color="#5d6a58"/>
        <stop offset="1" stop-color="#3f6a45"/>
      </linearGradient>
    </defs>
    <polygon points="0,46 506,0 506,95 0,143" fill="url(#dreamFill)"/>
  </svg>
  <h2 class="dream head abs">we help your dream<br>design come true.</h2>

  <h2 class="offer head abs">what servecies do we offer?</h2>
  <div class="label-rule abs" style="left:53px;top:551px;width:32px"></div>
  <span class="label abs" style="left:89px;top:547px">Our Services &amp; Works</span>
  <div class="list abs" style="left:181px;top:545px">1. Custom Furniture Design<br>2. Custom Furniture Make<br>3. Architectural Millwork<br>4. Kitchen Cabinetry</div>
  <div class="list abs" style="left:298px;top:545px">5. Kitchen Design<br>6. Make Over<br>7. Custom Designs<br>8. Custom Products</div>

  <section aria-label="Project gallery">
    <div class="tile" role="img" aria-label="Photo of a white minimal interior with a curved wall opening" style="left:70px;top:626px;width:183px;height:107px;background:linear-gradient(120deg,#d9d9d6 0%,#ededeb 35%,#f7f7f6 100%)"></div>
    <div class="tile" role="img" aria-label="Photo of a pale blue chaise sofa with a potted plant and pendant lamps" style="left:253px;top:626px;width:182px;height:107px;background:linear-gradient(180deg,#f2f2f2 0%,#e6e8e9 55%,#9fb0bb 75%,#dfe1e2 100%)"></div>
    <div class="tile" role="img" aria-label="Photo of a modern white kitchen with steel appliances" style="left:70px;top:733px;width:183px;height:103px;background:linear-gradient(180deg,#e9e9e9 0%,#9a9b9c 45%,#d8d9da 75%,#4d4f51 100%)"></div>
    <div class="tile" role="img" aria-label="Photo of a framed yellow poster over a beige sofa with pendant lamps" style="left:253px;top:733px;width:182px;height:103px;background:linear-gradient(180deg,#f4f4f3 0%,#eeece6 55%,#cfc8bb 85%,#b9b1a2 100%)"></div>
  </section>

  <h2 class="news head abs">latest news and articles<br>about custom furniture</h2>
  <div class="label-rule abs" style="left:59px;top:983px;width:32px"></div>
  <span class="label abs" style="left:95px;top:979px">Our Blog</span>
  <span class="post abs" style="left:179px;top:985px">Hello world!</span>
  <span class="date abs" style="left:383px;top:987px">May 14, 2024</span>
  <div class="abs" style="left:179px;top:995px;width:231px;height:.6px;background:var(--rule)"></div>

  <svg class="band abs" style="top:1020px" width="506" height="176" role="img" aria-label="Photo of a grey-blue living room with a large sofa and tall window">
    <defs>
      <linearGradient id="footFill" x1="0" y1="0" x2="0" y2="1">
        <stop offset="0" stop-color="#59646e"/>
        <stop offset=".55" stop-color="#46525c"/>
        <stop offset=".9" stop-color="#2e363e"/>
        <stop offset="1" stop-color="#1f2428"/>
      </linearGradient>
    </defs>
    <polygon points="0,46 506,0 506,176 0,176" fill="url(#footFill)"/>
  </svg>
  <h2 class="ready head abs">ready to start?</h2>
  <p class="ready-sub abs">A description about how the process of ordering works plu a direct link to order form and page to start order or be in touch</p>
  <a class="ready-btn btn abs">START YOUR PROJECT</a>

</div>
</body>
</html>
```